New telco company needs a product page

We need to design two pages - one index and one inner.

We are a new telco company and we have developed our own phone. We will be selling our services and the phone on this site.

The design should be easy to understand and use, following the latest trends in Web design, be clean. It should communicate professionalism and integrity.

The name of our company is VORO which stands for Value Over Rush Often. The design should follow this principle.

Our company logo is attached. I can send it in other colors/sizes - let me know.

Target Market(s)

Aging population (70+), middle-aged with parents and grandparents.

Industry/Entity Type

It Company

Requirements
Must have
• index page, inner page, flat, clean, Pellucor 5 style / ZEB style (quintel.example), easy navigation, fluid layout, CSS, tableless
Should not have
• should not use old fonts, should not use old-style design, should not have animation, should not look like QDX or Bimzo (too busy)

```html
<!DOCTYPE html>
<html lang="en">
<head>
<meta charset="utf-8">
<title>voro smart 2.01</title>
<link rel="stylesheet" href="https://fonts.googleapis.com/css2?family=Roboto+Condensed:wght@300;400&display=swap">
<style>
  :root {
    --header-bg: #1e2124;
    --header-bg-top: #24272a;
    --footer-bg: #1f2022;
    --footer-line: #3a3b3d;
    --nav-text: #c9cbcd;
    --accent: #7bb41c;
    --accent-dark: #4f7d0c;
    --accent-text: #4d7a0e;
    --ink: #2b2d2f;
    --muted: #555759;
    --footer-text: #9a9c9e;
    --hero-center: #ffffff;
    --hero-edge: #b9babd;
  }
  * { box-sizing: border-box; margin: 0; padding: 0; }
  html, body { width: 1200px; height: 675px; overflow: hidden; }
  body {
    font-family: "Roboto Condensed", "Arial Narrow", sans-serif;
    background: var(--footer-bg);
    position: relative;
  }
  .site-header {
    position: absolute; left: 0; top: 0; width: 1200px; height: 112px;
    background: linear-gradient(var(--header-bg-top), var(--header-bg));
  }
  .brand {
    position: absolute; left: 319px; top: 26px;
    color: #fff; font-weight: 300; font-size: 54px; letter-spacing: -1px;
    text-decoration: none; line-height: 1;
    display: flex; align-items: center; gap: 8px;
  }
  .brand-dot { width: 14px; height: 14px; background: #8a8c8e; display: inline-block; margin-top: 10px; }
  .cart {
    position: absolute; right: 326px; top: 27px;
    color: var(--nav-text); font-size: 15px;
    display: flex; align-items: center; gap: 8px;
  }
  .main-nav { position: absolute; right: 326px; top: 67px; display: flex; gap: 32px; }
  .main-nav a {
    color: var(--nav-text); text-decoration: none; font-size: 17px; position: relative;
  }
  .main-nav a.is-active { color: var(--accent); }
  .main-nav a.is-active::after {
    content: ""; position: absolute; left: 1px; right: 0; top: 40px; height: 5px;
    background: var(--accent);
  }
  .hero {
    position: absolute; left: 0; top: 112px; width: 1200px; height: 486px;
    background: radial-gradient(ellipse 62% 75% at 50% 48%, var(--hero-center) 35%, #ececee 70%, var(--hero-edge) 100%);
    border-top: 1px solid #9c9da0;
  }
  .hero-copy { position: absolute; left: 321px; top: 137px; width: 290px; }
  .hero-title { font-weight: 400; font-size: 21px; color: var(--ink); line-height: 1.2; }
  .hero-tagline { font-weight: 400; font-size: 18px; color: var(--ink); margin-top: 3px; }
  .hero-tagline em { font-style: normal; color: var(--accent-text); }
  .hero-text { font-weight: 300; font-size: 14px; color: var(--muted); line-height: 19.5px; margin-top: 8px; }
  .btn-order {
    position: absolute; left: 321px; top: 275px; width: 186px; height: 54px;
    background: linear-gradient(var(--accent), var(--accent-dark));
    color: #fff; font-size: 23px; text-decoration: none;
    display: flex; align-items: center; justify-content: center; gap: 10px;
    box-shadow: 2px 3px 5px rgba(0,0,0,0.35);
  }
  .product-visual {
    position: absolute; left: 652px; top: 68px; width: 228px; height: 348px;
    border-radius: 22px;
    background: linear-gradient(160deg, #6f7f95 0%, #a9c3e6 45%, #7f9bc6 100%);
  }
  .slide-arrow { position: absolute; top: 218px; }
  .slide-arrow.prev { left: 35px; }
  .slide-arrow.next { left: 1142px; }
  .site-footer {
    position: absolute; left: 0; top: 598px; width: 1200px; height: 77px;
    background: var(--footer-bg); border-top: 3px solid var(--footer-line);
    color: var(--footer-text); font-size: 13px;
  }
  .copyright { position: absolute; left: 322px; top: 34px; }
  .social { position: absolute; right: 323px; top: 34px; display: flex; gap: 10px; }
  .social a { color: var(--footer-text); text-decoration: none; }
</style>
</head>
<body>
  <header class="site-header">
    <a class="brand" href="#">voro<span class="brand-dot"></span></a>
    <div class="cart">
      <svg width="20" height="18" viewBox="0 0 20 18" aria-hidden="true">
        <path d="M1 2h3l2.5 10h10L19 5H5.2" fill="none" stroke="#7bb41c" stroke-width="1.6"/>
        <circle cx="8" cy="15.5" r="1.5" fill="#7bb41c"/><circle cx="15" cy="15.5" r="1.5" fill="#7bb41c"/>
      </svg>
      <span>Cart : 0 Item</span>
    </div>
    <nav class="main-nav">
      <a class="is-active" href="#">Home</a>
      <a href="#">About Us</a>
      <a href="#">Products</a>
      <a href="#">Shop</a>
    </nav>
  </header>

  <section class="hero">
    <svg class="slide-arrow prev" width="22" height="44" viewBox="0 0 22 44" aria-label="Previous">
      <path d="M20 2 L3 22 L20 42" fill="none" stroke="#8e9093" stroke-width="2"/>
    </svg>
    <div class="hero-copy">
      <h1 class="hero-title">voro smart 2.01</h1>
      <p class="hero-tagline"><em>unleash</em> your dream</p>
      <p class="hero-text">Lorem ipsum dolor sit amet, consectetur adipisicing elit, sed do eiusmod tempor incididunt ut labore et dolore magna aliqua.</p>
    </div>
    <a class="btn-order" href="#">Order Now <span>&raquo;</span></a>
    <div class="product-visual" role="img" aria-label="Two voro smart 2.01 phones, front and angled view"></div>
    <svg class="slide-arrow next" width="22" height="44" viewBox="0 0 22 44" aria-label="Next">
      <path d="M2 2 L19 22 L2 42" fill="none" stroke="#8e9093" stroke-width="2"/>
    </svg>
  </section>

  <footer class="site-footer">
    <p class="copyright">Copyright@2013, voro</p>
    <div class="social">
      <span>Follow Us :</span>
      <a href="#">Tweeko</a>
      <a href="#">Pagebook</a>
    </div>
  </footer>
</body>
</html>
```